LEARN Business Skills so you can Earn a good living

size of the poster is 8”x 10.75" plus 0.25" bleed.
Please leave 1 inch on the bottoum for footer
I want a design a poster that will attract people's attention.
I appreciate a creative ad however the ad should not take away from being able to clearly read the text.
-I also appreciate a simple creative ad that is not too busy.
-you can use graphics, vectors, or pictures of real people.
-however, if you use real people it should be a white male that is wearing a white shirt and look like a professional person.

Target Market(s)

Potential young business people

Industry/Entity Type

education

Requirements
Must have
• easy to read the text
Nice to have
• I would like a "creative" simple ad that is easy to be read
Should not have
• pictures of women

```html
<!DOCTYPE html>
<html lang="en">
<head>
<meta charset="utf-8">
<title>Learn It to Earn It – Business Enrichment Course</title>
<link href="https://fonts.googleapis.com/css2?family=Montserrat:wght@400;500;700;800&display=swap" rel="stylesheet">
<style>
  :root {
    --stage: #8a8a8a;
    --paper: #f1f1f1;
    --footer: #ffffff;
    --ink-mid: #6b6b6b;
    --ink-dark: #262626;
    --rule: #777777;
    --photo-top: #bdbdbd;
    --photo-mid: #d2d2d2;
    --photo-low: #e6e6e6;
  }
  html, body {
    margin: 0;
    width: 1200px;
    height: 1200px;
    overflow: hidden;
    background: var(--stage);
  }
  .poster {
    position: absolute;
    left: 169px;
    top: 20px;
    width: 862px;
    height: 1160px;
    background: var(--paper);
    font-family: "Montserrat", sans-serif;
    overflow: hidden;
  }
  .backdrop {
    position: absolute;
    left: 0; top: 0;
    width: 862px; height: 1052px;
  }
  .footer {
    position: absolute;
    left: 0; bottom: 0;
    width: 862px; height: 108px;
    background: var(--footer);
  }
  .photo {
    position: absolute;
    left: 0; top: 360px;
    width: 430px; height: 692px;
    background: linear-gradient(180deg, var(--photo-top) 0%, var(--photo-mid) 35%, var(--photo-low) 100%);
    border-top-left-radius: 40px;
    border-top-right-radius: 215px;
  }
  .headline-top {
    position: absolute;
    left: 118px; top: 72px;
    margin: 0;
    font-size: 111px;
    line-height: 1;
    font-weight: 800;
    color: var(--ink-mid);
    letter-spacing: -1px;
  }
  .headline-bottom {
    position: absolute;
    right: 54px; top: 188px;
    margin: 0;
    display: flex;
    align-items: baseline;
    gap: 21px;
    line-height: 1;
    color: var(--ink-dark);
    font-weight: 800;
  }
  .headline-bottom .small { font-size: 80px; letter-spacing: -1px; }
  .headline-bottom .big { font-size: 111px; letter-spacing: -1px; }
  .accent-rule {
    position: absolute;
    left: 802px; top: 331px;
    width: 4px; height: 275px;
    background: var(--rule);
  }
  .course-title {
    position: absolute;
    right: 86px; top: 323px;
    margin: 0;
    text-align: right;
    font-size: 69px;
    line-height: 68px;
    font-weight: 400;
    color: var(--ink-mid);
  }
  .tagline {
    position: absolute;
    right: 86px; top: 534px;
    margin: 0;
    text-align: right;
    font-size: 27px;
    line-height: 40px;
    font-weight: 500;
    color: var(--ink-mid);
  }
  .benefits-intro, .benefits, .subjects {
    position: absolute;
    right: 54px;
    margin: 0;
    text-align: right;
    color: var(--ink-mid);
    font-weight: 500;
  }
  .benefits-intro { top: 652px; font-size: 19px; line-height: 27px; }
  .benefits { top: 715px; font-size: 19.5px; line-height: 27px; }
  .benefits strong { font-weight: 700; }
  .subjects { top: 810px; font-size: 17px; line-height: 24px; white-space: nowrap; }
</style>
</head>
<body>
<main class="poster">
  <svg class="backdrop" viewBox="0 0 862 1052" aria-hidden="true">
    <polygon points="0,330 330,0 470,0 0,470" fill="#f6f6f6"/>
    <polygon points="120,1052 862,310 862,420 230,1052" fill="#f5f5f5"/>
    <polygon points="560,1052 862,750 862,850 660,1052" fill="#f7f7f7"/>
  </svg>

  <div class="photo" role="img" aria-label="Photo of a smiling young professional man in glasses and a white shirt, arms crossed"></div>

  <h1 class="headline-top">LEARN IT</h1>
  <p class="headline-bottom"><span class="small">to</span><span class="big">EARN IT</span></p>

  <div class="accent-rule"></div>
  <h2 class="course-title">Business<br>Enrichment<br>Course</h2>
  <p class="tagline">A proven success of helping<br>people in their livelihoods</p>

  <p class="benefits-intro">Business skills that<br>will help you:</p>
  <p class="benefits"><strong>Get a quality job</strong> - start/grow your<br>business-Increase your salary</p>

  <p class="subjects">
    Business Admiistration – Small Business<br>
    Management - Finance - Investments -<br>
    Computers- Accounting - Sales&nbsp; Marketing -<br>
    Project Management Interviewing Skills -<br>
    Business Law -negotiation – Public Speaking - &nbsp; -<br>
    Import/export - Information Technoloy -<br>
    distribution - Marketing - &nbsp; Tallybook - Real<br>
    Estate - Health Care-management - Marketnest
  </p>

  <div class="footer"></div>
</main>
</body>
</html>
```